Stonelynk Business Card Design

The Stonelynk Co is an aggregate (crushing) equipment dealer serving Western Canadian provinces. Stonelynk is a distributor of aggregate equipment for different manufacturers.

We are looking to change and update the existing business card which has been used since the existence of the company. A copy of existing card has been attached for reference. The Stonelynk Co logo we want to remain the same and we want the green color to remain the same.

We are wanting something new with a different look. A refreshing card to show a new modern and updated look. No longer wanting to have the manufacturers on the back of the card but something more like our logo on the back of the card with a statement like "Crushing Solutions"

ideas could be:
- card can be different colors on front and back
- front or reverse of the card could possibly be the green color with the logo in black

Target Market(s)

Owners of Aggregate/Crushing companies

Requirements
Must have
• - logo to remain same along with same font within logo
• - green color to remain same
Nice to have
• as noted above under project description
Should not have

```html
<!DOCTYPE html>
<html lang="en">
<head>
<meta charset="utf-8">
<title>The Stonelynk Co – Business Card</title>
<link rel="stylesheet" href="https://fonts.googleapis.com/css2?family=Carlito:wght@400;700&display=swap">
<style>
  :root {
    --stage: #e4e4e6;
    --card-black: #0f0f0f;
    --brand-green: #a29f17;
    --brand-green-deep: #8d8a10;
    --ink-white: #ffffff;
    --ink-dark: #141414;
  }
  * { box-sizing: border-box; margin: 0; padding: 0; }
  html, body { width: 1200px; height: 1200px; overflow: hidden; }
  body {
    background: var(--stage);
    font-family: "Carlito", "Calibri", sans-serif;
    position: relative;
  }
  .card {
    position: absolute;
    width: 700px;
    height: 400px;
    left: 250px;
    overflow: hidden;
    box-shadow: 0 10px 24px rgba(0,0,0,0.18);
    background: var(--card-black);
  }
  .card--front { top: 130px; }
  .card--back { top: 650px; }

  .front-bands { position: absolute; inset: 0; }

  .brand {
    position: absolute;
    display: flex;
    align-items: center;
    gap: 12px;
    white-space: nowrap;
  }
  .brand__dot {
    width: 26px; height: 26px;
    border-radius: 50%;
    background: var(--brand-green);
    flex: none;
  }
  .brand__name {
    color: var(--ink-white);
    font-weight: 700;
    font-size: 28px;
    letter-spacing: 0.5px;
  }
  .card--front .brand { left: 44px; top: 64px; }

  .address { position: absolute; left: 44px; top: 150px; font-size: 19px; line-height: 1.3; color: var(--ink-white); }
  .address__label { color: var(--brand-green); }

  .person { position: absolute; left: 400px; top: 150px; }
  .person__name {
    color: var(--brand-green);
    font-weight: 700;
    font-size: 36px;
    letter-spacing: 0.5px;
    margin-bottom: 8px;
  }
  .contact { display: grid; grid-template-columns: 58px auto; font-size: 19px; line-height: 1.3; }
  .contact dt { color: var(--brand-green); }
  .contact dd { color: var(--ink-white); }

  .back-brand-panel {
    position: absolute; left: 0; top: 0;
    width: 315px; height: 400px;
    background: var(--card-black);
  }
  .card--back .brand { left: 34px; top: 164px; }
  .card--back .brand__name { font-size: 24px; }
  .back-address {
    position: absolute; left: 34px; top: 206px;
    color: var(--ink-white); font-size: 15px;
    white-space: nowrap;
  }
  .back-statement {
    position: absolute; left: 315px; top: 0;
    width: 385px; height: 400px;
    background: linear-gradient(135deg, var(--brand-green) 0%, var(--brand-green-deep) 100%);
    display: flex;
    flex-direction: column;
    justify-content: center;
    padding: 0 40px;
  }
  .statement__rule {
    width: 64px; height: 6px;
    background: var(--ink-dark);
    margin-bottom: 20px;
  }
  .statement__text {
    font-size: 46px;
    font-weight: 700;
    line-height: 1.05;
    letter-spacing: 1.5px;
    color: var(--ink-dark);
  }
</style>
</head>
<body>

<section class="card card--front" aria-label="Business card front">
  <svg class="front-bands" viewBox="0 0 700 400" width="700" height="400" aria-hidden="true">
    <polygon points="0,268 300,268 288,284 0,284" fill="var(--brand-green)"/>
    <polygon points="0,300 278,300 266,316 0,316" fill="var(--brand-green)"/>
    <polygon points="318,352 700,352 700,400 290,400" fill="var(--brand-green)"/>
  </svg>

  <div class="brand">
    <span class="brand__dot"></span>
    <span class="brand__name">THE STONELYNK CO.</span>
  </div>

  <p class="address">
    <span class="address__label">Address:</span><br>
    2218-48B Avenue<br>
    Camrose, AB T4V 1K6
  </p>

  <div class="person">
    <h1 class="person__name">DALE MARSTEN</h1>
    <dl class="contact">
      <dt>Tel</dt><dd>: 780.555.0142</dd>
      <dt>Fax</dt><dd>: 780.555.0187</dd>
      <dt>Direct</dt><dd>: 780.555.0163</dd>
      <dt>Email</dt><dd>: dale@stonelynk.com</dd>
      <dt>Web</dt><dd>: www.stonelynk.ca</dd>
    </dl>
  </div>
</section>

<section class="card card--back" aria-label="Business card back">
  <div class="back-brand-panel">
    <div class="brand">
      <span class="brand__dot"></span>
      <span class="brand__name">THE STONELYNK CO.</span>
    </div>
    <p class="back-address">2218-48B Avenue, Camrose, AB T4V 1K6</p>
  </div>

  <div class="back-statement">
    <span class="statement__rule"></span>
    <h2 class="statement__text">CRUSHING<br>SOLUTIONS</h2>
  </div>
</section>

</body>
</html>
```